Build a personal mobile responsive super creative website

Hi!

I would like a personal website to share my world with the internet community. My passions are new technology & engineering, writing quotes and photography. Unfortunately, I do not have any design and creative skills. For this reason, I need a good and super creative web designer to build me a fully mobile responsive website with an attractive design. I don't like standard websites :P I don't mind templates, as soon as it looks unique on my webpage.
I am not on a rush, I just want it to look super cool :)
Happy to see your proposals :D

Pages:
-Home
-About
-Gallery
-Quotes
-Blog

```html
<!DOCTYPE html>
<html lang="en">
<head>
<meta charset="utf-8">
<title>Fernway — Personal Blog</title>
<link href="https://fonts.googleapis.com/css2?family=Raleway:wght@200;300;400;600;700&family=Open+Sans:wght@400;600&family=Lora:ital@1&display=swap" rel="stylesheet">
<style>
:root{
  --nav:#323232;
  --footer:#3a3a3a;
  --band:#eeeeee;
  --ink:#444444;
  --muted:#8a8a8a;
  --body:#777777;
  --link:#2a78b4;
  --accent:#d83a32;
  --white:#ffffff;
  --line:#dddddd;
}
*{margin:0;padding:0;box-sizing:border-box}
html,body{width:1200px;height:3355px;overflow:hidden;background:var(--white)}
body{position:relative;font-family:'Open Sans',Arial,sans-serif;color:var(--body);font-size:9px;line-height:14.5px}
.abs{position:absolute}
.serif{font-family:'Lora',Georgia,serif;font-style:italic}
.section-title{position:absolute;font-family:'Raleway',Arial,sans-serif;font-weight:300;font-size:25px;color:var(--ink);letter-spacing:.5px;text-transform:uppercase}
.small-title{position:absolute;font-family:'Raleway',Arial,sans-serif;font-weight:600;font-size:17px;color:#333;text-transform:uppercase}

.site-nav{position:absolute;left:0;top:0;width:1200px;height:93px;background:var(--nav)}
.brand{position:absolute;left:229px;top:41px;font-family:'Raleway',Arial,sans-serif;font-weight:700;font-size:19px;color:var(--white);letter-spacing:.5px}
.menu{position:absolute;top:47px;font-family:'Raleway',Arial,sans-serif;font-weight:700;font-size:9px;color:var(--white);letter-spacing:.3px}

.hero{position:absolute;left:0;top:93px;width:1200px;height:657px;background:linear-gradient(180deg,#d9cfac 0%,#c8b783 35%,#a28a50 62%,#8a7546 80%,#b09a5c 100%)}
.hero-title{position:absolute;left:0;width:1200px;top:373px;text-align:center;font-family:'Raleway',Arial,sans-serif;font-weight:200;font-size:39px;line-height:46px;color:var(--white)}
.hero-sub{position:absolute;left:0;width:1200px;top:418px;text-align:center;font-family:'Raleway',Arial,sans-serif;font-size:9px;color:var(--white)}
.hero-btn{position:absolute;left:571px;top:450px;width:68px;height:26px;border:1px solid var(--white);color:var(--white);font-size:10px;line-height:24px;text-align:center}

.band{position:absolute;left:0;width:1200px;background:var(--band)}
.stat{position:absolute;width:160px;text-align:center}
.stat-num{font-family:'Raleway',Arial,sans-serif;font-weight:700;font-size:34px;line-height:36px;color:#3a3a3a;margin-top:6px}
.stat-label{font-size:8px;color:var(--muted);text-transform:uppercase}

.para{position:absolute;width:180px;font-size:9px;line-height:14.6px;color:var(--body)}
.photo{position:absolute;background:linear-gradient(135deg,#cfcfcf,#6e6e6e)}
.cat-link{position:absolute;left:256px;font-size:9px;color:var(--link)}
.post-col{position:absolute;width:175px;border-top:2px solid #333;padding-top:10px}
.post-title{font-size:15px;line-height:16px;color:var(--link)}
.date-dot{display:inline-block;width:26px;height:26px;border-radius:50%;background:#333;color:#fff;font-size:8px;line-height:26px;text-align:center;vertical-align:middle}

.avatar{position:absolute;border-radius:50%;background:linear-gradient(135deg,#e2e2e2,#8c8c8c)}
.blue-name{position:absolute;font-family:'Raleway',Arial,sans-serif;font-weight:700;font-size:14px;color:var(--link);text-transform:uppercase}
.tags{position:absolute;font-size:8.5px;line-height:13px;color:var(--link)}
.art-title{position:absolute;font-size:14px;line-height:19px;color:var(--link)}
.mini-date{position:absolute;font-size:8px;color:var(--muted)}
.mini-title{position:absolute;font-size:14px;line-height:18px;color:var(--link)}

.arch{position:absolute;font-size:8.5px;line-height:12px;color:var(--body)}
.arch span{display:block;font-size:7.5px;color:#aaa}
.author{position:absolute;left:229px;width:160px;font-size:8.5px;color:var(--body)}
.author b{float:right;font-weight:400;color:#aaa}

.filters{position:absolute;left:0;width:1200px;text-align:center;top:2717px;font-size:12px;color:#666}
.filters span{margin:0 10px}

.tile{position:absolute;width:171px;height:139px}

.site-footer{position:absolute;left:0;top:3115px;width:1200px;height:240px;background:var(--footer)}
.foot-head{position:absolute;top:50px;font-family:'Raleway',Arial,sans-serif;font-weight:700;font-size:16px;color:var(--white)}
.foot-text{position:absolute;font-size:8.5px;line-height:15px;color:#d6d6d6}
.social{position:absolute;left:815px;width:175px;height:29px;border:1px solid #5a5a5a;font-size:8.5px;line-height:27px;color:#ddd;padding-left:38px}
.social i{position:absolute;left:0;top:0;width:29px;height:27px;border-right:1px solid #5a5a5a}
.social b{position:absolute;right:10px;font-weight:400;color:#999}
.media-dot{position:absolute;width:29px;height:29px;border-radius:50%;background:linear-gradient(135deg,#bbb,#555)}
</style>
</head>
<body>

<header class="site-nav">
  <div class="brand">FERNWAY</div>
  <div class="menu" style="left:660px">HOME</div>
  <div class="menu" style="left:705px">ABOUT ▾</div>
  <div class="menu" style="left:767px">PORTFOLIO ▾</div>
  <div class="menu" style="left:848px">BLOG ▾</div>
  <div class="menu" style="left:903px">QUOTES</div>
  <svg class="abs" style="left:958px;top:48px" width="20" height="10" viewBox="0 0 20 10"><circle cx="4" cy="4" r="3" fill="none" stroke="#fff" stroke-width="1.5"/><line x1="6" y1="6" x2="9" y2="9" stroke="#fff" stroke-width="1.5"/><path d="M13 3l3 3 3-3" fill="#fff"/></svg>
</header>

<section class="hero" role="img" aria-label="Hazy aerial view of a city skyline above a river glowing in golden light"></section>
<div class="hero-title">BASED ON GRIDSTRAP</div>
<div class="hero-sub">TO COVER ALL THE WEB DEVELOPMENT CASES</div>
<div class="hero-btn serif">Download</div>

<section class="band" style="top:750px;height:125px">
  <div class="stat" style="left:270px;top:24px">
    <svg width="20" height="18" viewBox="0 0 20 18"><rect x="1" y="4" width="18" height="13" rx="2" fill="none" stroke="#444" stroke-width="1.5"/><circle cx="10" cy="10.5" r="3.5" fill="none" stroke="#444" stroke-width="1.5"/><path d="M6 4l2-3h4l2 3" fill="none" stroke="#444" stroke-width="1.5"/></svg>
    <div class="stat-num">161</div><div class="stat-label">Photos added</div>
  </div>
  <div class="stat" style="left:530px;top:24px">
    <svg width="20" height="18" viewBox="0 0 20 18"><path d="M1 3l6-2 6 2 6-2v14l-6 2-6-2-6 2z M7 1v14 M13 3v14" fill="none" stroke="#444" stroke-width="1.5"/></svg>
    <div class="stat-num">0</div><div class="stat-label">Places visited</div>
  </div>
  <div class="stat" style="left:790px;top:24px">
    <svg width="20" height="18" viewBox="0 0 20 18"><rect x="4" y="1" width="12" height="16" fill="none" stroke="#444" stroke-width="1.5"/><path d="M7 6h6M7 9h6M7 12h6" stroke="#444" stroke-width="1.2"/></svg>
    <div class="stat-num">119</div><div class="stat-label">Posts written</div>
  </div>
</section>

<h2 class="section-title" style="left:229px;top:888px">Photos</h2>
<h2 class="section-title" style="left:424px;top:888px">Overview</h2>
<h2 class="section-title" style="left:620px;top:888px">Latest blog posts</h2>

<svg class="abs" style="left:284px;top:938px" width="112" height="126" viewBox="0 0 112 126" role="img" aria-label="Portrait photo of a man in a six-sided frame"><defs><linearGradient id="portraitFill" x1="0" y1="0" x2="1" y2="1"><stop offset="0" stop-color="#e4e4e4"/><stop offset="1" stop-color="#7a7a7a"/></linearGradient></defs><polygon points="56,0 112,31 112,95 56,126 0,95 0,31" fill="url(#portraitFill)"/></svg>
<div class="photo" style="left:237px;top:1073px;width:31px;height:31px" role="img" aria-label="Thumbnail portrait"></div>
<div class="photo" style="left:279px;top:1073px;width:31px;height:31px" role="img" aria-label="Thumbnail portrait"></div>
<div class="photo" style="left:320px;top:1073px;width:31px;height:31px" role="img" aria-label="Thumbnail portrait"></div>
<div class="photo" style="left:361px;top:1073px;width:31px;height:31px;border-radius:50%" role="img" aria-label="Thumbnail portrait"></div>

<div class="cat-link" style="top:1187px">Photos</div>
<div class="cat-link" style="top:1207px">Logotypes</div>
<div class="cat-link" style="top:1227px">Mobile Apps</div>
<div class="cat-link" style="top:1247px">Prints</div>
<div class="cat-link" style="top:1267px">Interiors</div>
<div class="cat-link" style="top:1287px">Typography</div>
<div class="cat-link" style="top:1307px">Misc</div>

<p class="para" style="left:424px;top:935px">Cras pharetra suscipit tempus. Morbi egestas velit quis suscipit consectetur. Donec augue mauris, eleifend ut elit non, lobortis vulputate elit. In a lectus et tortor tempor facilisis. Nulla aliquet metus ut nibh commodo commodo.</p>
<p class="para" style="left:424px;top:1029px">Cras pharetra suscipit tempus. Morbi egestas velit quis suscipit consectetur. Donec augue mauris, eleifend ut elit non, lobortis vulputate elit. In a lectus et tortor tempor facilisis. Nulla aliquet metus ut nibh commodo commodo.</p>
<p class="para" style="left:424px;top:1124px">Cras pharetra suscipit tempus. Morbi egestas velit quis suscipit consectetur. Donec augue mauris, eleifend ut elit non, lobortis vulputate elit. In a lectus et tortor tempor facilisis. Nulla aliquet metus ut nibh commodo commodo.</p>
<p class="para" style="left:424px;top:1219px">Cras pharetra suscipit tempus. Morbi egestas velit quis suscipit consectetur. Donec augue mauris, eleifend ut elit non, lobortis vulputate elit. In a lectus et tortor tempor facilisis. Nulla aliquet metus ut nibh commodo commodo.</p>
<div class="abs serif" style="left:424px;top:1316px;font-size:22px;color:var(--accent);font-style:normal;font-weight:700">”</div>
<p class="abs serif" style="left:451px;top:1321px;width:150px;font-size:11.5px;line-height:18px;color:#444">Donec augue mauris, eleifend ut elit non, lobortis vulputate elit. In a lectus et tortor tempor facilisis. Nulla aliquet metus ut nibh commodo commodo!</p>

<article class="post-col" style="left:620px;top:940px">
  <div class="post-title serif">Far far away, behind the word ...</div>
  <div style="margin-top:8px"><span class="date-dot">15</span> <span style="display:inline-block;vertical-align:middle;font-size:8px;line-height:11px;margin-left:6px"><span class="serif">2014 Jun, 14</span><br><span class="serif" style="color:#444">by Lena Marwood</span></span></div>
  <p style="margin-top:12px;font-size:9px;line-height:14.6px">Cras pharetra suscipit tempus. Morbi egestas velit quis suscipit consectetur. Donec augue mauris, eleifend ut elit non, lobortis vulputate elit. In a lectus et tortor tempor facilisis. Nulla aliquet metus ut nibh commodo commodo.</p>
</article>
<article class="post-col" style="left:815px;top:940px">
  <div class="post-title serif">Nobody knows it.<br>Start immidiately.</div>
  <div style="margin-top:8px"><span class="date-dot">23</span> <span style="display:inline-block;vertical-align:middle;font-size:8px;line-height:11px;margin-left:6px"><span class="serif">2014 Jun, 14</span><br><span class="serif" style="color:#444">by Lena Marwood</span></span></div>
  <p style="margin-top:12px;font-size:9px;line-height:14.6px">Cras pharetra suscipit tempus. Morbi egestas velit quis suscipit consectetur. Donec augue mauris, eleifend ut elit non, lobortis vulputate elit. In a lectus et tortor tempor facilisis. Nulla aliquet metus ut nibh commodo commodo.</p>
</article>

<h2 class="section-title" style="left:620px;top:1180px">Interesting</h2>
<div class="abs" style="left:620px;top:1227px;width:370px;height:248px;background:linear-gradient(90deg,#e9e9e9 0%,#d0d0d0 38%,#8c8c8c 55%,#3e3e3e 80%,#777 100%)" role="img" aria-label="Black and white portrait of a woman in a slider"></div>
<div class="abs" style="left:620px;top:1339px;width:32px;height:32px;background:rgba(255,255,255,.25);color:#fff;text-align:center;line-height:32px;font-size:12px">‹</div>
<div class="abs" style="left:958px;top:1339px;width:32px;height:32px;background:rgba(255,255,255,.25);color:#fff;text-align:center;line-height:32px;font-size:12px">›</div>

<section class="band" style="top:1511px;height:366px">
  <h2 class="section-title" style="left:0;width:1200px;text-align:center;top:60px">Customer's review</h2>
  <div class="avatar" style="left:334px;top:113px;width:98px;height:98px" role="img" aria-label="Portrait of the reviewer"></div>
  <div class="abs" style="left:283px;width:200px;top:219px;text-align:center;font-family:'Raleway',Arial,sans-serif;font-size:16px;color:#444">Clara Voss</div>
  <div class="abs" style="left:283px;width:200px;top:246px;text-align:center;font-size:8px;color:var(--muted)">Business Analytics Specialist</div>
  <div class="abs serif" style="left:467px;top:110px;font-size:24px;color:var(--accent);font-style:normal;font-weight:700">”</div>
  <div class="abs" style="left:467px;top:136px;font-family:'Raleway',Arial,sans-serif;font-size:15px;color:#333">GOOD WORK!</div>
  <p class="abs" style="left:467px;top:160px;width:440px;font-size:8.5px;line-height:14.6px">During the spring and summer of 1977, Port Elden's city and metro councils were under pressure to do something about the shops and venues that were housed in the area along the main street from the harbor to the old square following a sad event that shook the town. The crisis was more political than real; nevertheless, under pressure from the mayor and council, the planners had to plan and implement a neighbourhood sweep on the scale of the earlier district reform.</p>
  <div class="abs" style="left:467px;top:240px;font-size:17px;letter-spacing:3px;color:#999">★★★★</div>
</section>

<h3 class="small-title" style="left:229px;top:1892px">Archives</h3>
<div class="abs" style="left:229px;top:1952px;width:78px;height:38px;background:#eaeaea"></div>
<div class="arch" style="left:240px;top:1922px">May 2014<span>4 entries</span></div>
<div class="arch" style="left:320px;top:1922px">Apr. 2014<span>4 entries</span></div>
<div class="arch" style="left:240px;top:1958px">Mar. 2014<span>2 entries</span></div>
<div class="arch" style="left:320px;top:1958px">Feb. 2014<span>7 entries</span></div>
<div class="arch" style="left:240px;top:1995px">Jan. 2014<span>1 entry</span></div>
<div class="arch" style="left:320px;top:1995px">Dec. 2013<span>6 entries</span></div>
<div class="arch" style="left:240px;top:2031px">Nov.2013<span>3 entries</span></div>
<div class="arch" style="left:320px;top:2031px">Oct. 2013<span>4 entries</span></div>
<div class="arch" style="left:240px;top:2068px">Sep. 2013<span>5 entries</span></div>
<div class="arch" style="left:320px;top:2068px">Aug. 2013<span>5 entries</span></div>
<div class="arch" style="left:240px;top:2104px">Jul. 2013<span>2 entries</span></div>

<h3 class="small-title" style="left:229px;top:2170px">Authors</h3>
<div class="author" style="top:2196px">Jane Ardley<b>124</b></div>
<div class="author" style="top:2219px">Clara Voss<b>45 876</b></div>
<div class="author" style="top:2241px">David Reeve<b>546</b></div>
<div class="author" style="top:2264px">Jina (Zina)<b>1 235</b></div>
<div class="author" style="top:2287px">Milo Kessler Jr.<b>4 345</b></div>
<div class="author" style="top:2309px">Felicia Moran<b>12</b></div>
<div class="author" style="top:2332px">Morgan Hale<b>665</b></div>
<div class="author" style="top:2355px">Anna Lindqvist<b>227</b></div>
<div class="author" style="top:2378px">Julio Serrat<b>45</b></div>
<div class="author" style="top:2400px">Mikola Varga<b>2 456</b></div>
<div class="author" style="top:2423px">Jen Tao<b>2</b></div>
<div class="author" style="top:2446px">Megan Lee Ashby<b>349</b></div>

<h2 class="section-title" style="left:424px;top:1890px">Articles</h2>
<div class="avatar" style="left:424px;top:1943px;width:99px;height:99px" role="img" aria-label="Author portrait"></div>
<div class="blue-name" style="left:547px;top:1951px">Nora Vale</div>
<div class="tags" style="left:547px;top:1976px;width:150px">Gadgets, Relaxation, Sports, Glamour, Design, Rumors<br>noravale.example</div>
<div class="avatar" style="left:717px;top:1943px;width:99px;height:99px" role="img" aria-label="Author portrait"></div>
<div class="blue-name" style="left:839px;top:1951px">Ilse Brandt</div>
<div class="tags" style="left:839px;top:1976px;width:155px">Gadgets, Relaxation, Sports, Glamour, Design, Rumors<br>ilsebrandt.example</div>

<div class="art-title serif" style="left:424px;top:2059px;width:260px">In 1965, Corner Nine bought some of the machines and services</div>
<p class="para" style="left:424px;top:2106px;width:275px">Land register data, which excludes lakes, ponds, glaciers and river estuaries, lists the village as a small commune in the hill country. Buildings include an old abbey and a priory built by its first abbot, which was at first a simple priory, and later a house of secular canonesses from the local nobility of the region.</p>
<div class="art-title serif" style="left:717px;top:2059px;width:260px">The Room Dedication Program has recently been implemented</div>
<p class="para" style="left:717px;top:2106px;width:275px">The Harrow Inn is a 151-room historic hotel located 50 miles north of the city on the banks of the river. It is named after the founder of the nearby academy and its first head. The inn has three main markets: tourists visiting the town, weddings, and corporate conferences.</p>

<div class="avatar" style="left:424px;top:2262px;width:45px;height:45px"></div>
<div class="mini-date serif" style="left:427px;top:2311px">2014 Jun, 14</div>
<div class="mini-title serif" style="left:489px;top:2262px;width:120px">In 1965, Corner Nine bought some</div>
<p class="para" style="left:489px;top:2310px;width:110px">The system utilised prefabricated light gauge steel frames which could be built economically up to a maximum of 4 storeys.</p>

<div class="avatar" style="left:620px;top:2262px;width:45px;height:45px"></div>
<div class="mini-date serif" style="left:623px;top:2311px">2014 Jun, 14</div>
<div class="mini-title serif" style="left:685px;top:2262px;width:120px">New Plays from Europe</div>
<p class="para" style="left:685px;top:2310px;width:110px">(December 22, 1886 – July 23, 1947), was a poet, philosopher and academic. He should not be confused with David Reeve, a contemporary writer.</p>

<div class="avatar" style="left:815px;top:2262px;width:45px;height:45px"></div>
<div class="mini-date serif" style="left:818px;top:2311px">2014 Jun, 14</div>
<div class="mini-title serif" style="left:880px;top:2262px;width:120px">The South West Coast</div>
<p class="para" style="left:880px;top:2310px;width:110px">The system utilised prefabricated light gauge steel frames which could be built economically up to a maximum of 4 storeys.</p>

<div class="avatar" style="left:424px;top:2451px;width:45px;height:45px"></div>
<div class="mini-date serif" style="left:427px;top:2500px">2014 Jun, 14</div>
<div class="mini-title serif" style="left:489px;top:2451px;width:120px">In 1965, Corner Nine bought some</div>
<p class="para" style="left:489px;top:2499px;width:110px">(December 22, 1886 – July 23, 1947), was a poet, philosopher and academic. He should not be confused with David Reeve, a contemporary writer.</p>

<div class="avatar" style="left:620px;top:2451px;width:45px;height:45px"></div>
<div class="mini-date serif" style="left:623px;top:2500px">2014 Jun, 14</div>
<div class="mini-title serif" style="left:685px;top:2451px;width:120px">New Plays from Europe</div>
<p class="para" style="left:685px;top:2499px;width:110px">The system utilised prefabricated light gauge steel frames which could be built economically up to a maximum of 4 storeys.</p>

<div class="avatar" style="left:815px;top:2451px;width:45px;height:45px"></div>
<div class="mini-date serif" style="left:818px;top:2500px">2014 Jun, 14</div>
<div class="mini-title serif" style="left:880px;top:2451px;width:120px">The South West Coast</div>
<p class="para" style="left:880px;top:2499px;width:110px">The system utilised prefabricated light gauge steel frames which could be built economically up to a maximum of 4 storeys.</p>

<h2 class="section-title" style="left:0;width:1200px;text-align:center;top:2665px">Featured portfolio</h2>
<div class="filters serif"><span>All</span><span>Web Design</span><span>Online Marketing</span></div>
<div class="tile" style="left:239px;top:2772px;background:linear-gradient(135deg,#eee,#222)" role="img" aria-label="Close-up of a horse head"></div>
<div class="tile" style="left:430px;top:2772px;background:linear-gradient(135deg,#888,#ddd)" role="img" aria-label="Steel structure of a building"></div>
<div class="tile" style="left:620px;top:2772px;background:linear-gradient(135deg,#444,#999)" role="img" aria-label="Old wooden door"></div>
<div class="tile" style="left:811px;top:2772px;background:linear-gradient(180deg,#f2f2f2,#333)" role="img" aria-label="Tall grass"></div>
<div class="tile" style="left:239px;top:2932px;background:linear-gradient(135deg,#ddd,#555)" role="img" aria-label="Fox portrait"></div>
<div class="tile" style="left:430px;top:2932px;background:linear-gradient(135deg,#333,#aaa)" role="img" aria-label="Skewers on a grill"></div>
<div class="tile" style="left:620px;top:2932px;background:linear-gradient(135deg,#777,#ccc)" role="img" aria-label="Baked cookies"></div>
<div class="tile" style="left:811px;top:2932px;background:linear-gradient(135deg,#ccc,#777)" role="img" aria-label="Pastries on a plate"></div>

<footer class="site-footer">
  <div class="abs" style="left:583px;top:-16px;width:53px;height:16px;background:var(--footer)"></div>
  <svg class="abs" style="left:605px;top:-12px" width="9" height="11" viewBox="0 0 9 11"><path d="M4.5 0a4 4 0 0 1 4 4c0 3-4 7-4 7s-4-4-4-7a4 4 0 0 1 4-4z" fill="#fff"/><circle cx="4.5" cy="4" r="1.5" fill="#3a3a3a"/></svg>

  <div class="foot-head" style="left:229px">FERNWAY</div>
  <p class="foot-text" style="left:229px;top:80px;width:180px">Room Of Echoes was originally going to be released as a side-project that Dorran embarked on with songwriter and producer Tomas Reil, known for his work with Owen Marsh, but both decided that due to the variety of tracks, Dorran should release it as his third solo...</p>

  <div class="foot-head" style="left:424px">CONTACTS</div>
  <svg class="abs" style="left:424px;top:84px" width="10" height="9" viewBox="0 0 10 9"><path d="M5 0l5 4H8v5H2V4H0z" fill="#ccc"/></svg>
  <p class="foot-text" style="left:441px;top:80px;width:150px">480 Harbor Lane - 12, Eastfield, USA</p>
  <svg class="abs" style="left:424px;top:118px" width="9" height="9" viewBox="0 0 9 9"><path d="M1 0h2l1 2-1 1a5 5 0 0 0 3 3l1-1 2 1v2a1 1 0 0 1-1 1A8 8 0 0 1 0 1a1 1 0 0 1 1-1z" fill="#ccc"/></svg>
  <p class="foot-text" style="left:441px;top:114px">1 555 010 24 68</p>
  <svg class="abs" style="left:424px;top:145px" width="10" height="8" viewBox="0 0 10 8"><rect x="0" y="0" width="10" height="8" fill="#ccc"/><path d="M0 0l5 4 5-4" fill="none" stroke="#3a3a3a"/></svg>
  <p class="foot-text" style="left:441px;top:141px;text-decoration:underline">hello@fernway.example</p>

  <div class="foot-head" style="left:620px">MEDIA</div>
  <div class="media-dot" style="left:620px;top:93px"></div>
  <div class="media-dot" style="left:664px;top:93px;background:linear-gradient(135deg,#e8a,#ca4)"></div>
  <div class="media-dot" style="left:708px;top:93px"></div>
  <div class="media-dot" style="left:752px;top:93px"></div>
  <div class="media-dot" style="left:620px;top:126px"></div>
  <div class="media-dot" style="left:664px;top:126px"></div>
  <div class="media-dot" style="left:708px;top:126px"></div>
  <div class="media-dot" style="left:752px;top:126px"></div>
  <div class="media-dot" style="left:620px;top:160px"></div>
  <div class="media-dot" style="left:664px;top:160px"></div>

  <div class="foot-head" style="left:815px">FOLLOW US</div>
  <div class="social" style="top:90px"><i></i>CHIRPER<b>324</b></div>
  <div class="social" style="top:125px"><i></i>FRIENDPAGE<b>653</b></div>
  <div class="social" style="top:160px"><i></i>WORKLINK<b>234</b></div>
</footer>

</body>
</html>
```